Harborline Crest Insurance Services

we are a high end insurance agency we specialize on Auto | Home | Business | Life looking for something professional and luxuries at the same time. if you guys need anything else please let me know.

Auto | Home | Business | Life must be under logo on the back with black background.

i want the back part to be black with our gold logo on it.

Target Market(s)

Auto | Home | Business | Life

Industry/Entity Type

Insurance Broker

Contact Information for Business Card

My logo is gold so a black in the back would be nice.

Font styles to use
Serif

Colors
000000

Requirements
Must have
• Big logo on the back with black background.

```html
<!DOCTYPE html>
<html lang="en">
<head>
<meta charset="utf-8">
<title>Harborline Crest Insurance Services – Business Card</title>
<link rel="stylesheet" href="https://fonts.googleapis.com/css2?family=Libre+Baskerville:ital@0;1&family=Roboto:wght@400;500&display=swap">
<style>
  :root {
    --page: #e4e1dc;
    --card-black: #0e0e0e;
    --card-charcoal: #232323;
    --gold: #e8b423;
    --gold-soft: #d6a82a;
    --yellow: #f5c829;
    --silver-light: #e9e9e9;
    --silver-dark: #8c8c8c;
    --text-light: #f2f2f2;
    --ink: #1a1a1a;
  }
  * { box-sizing: border-box; margin: 0; padding: 0; }
  html, body { width: 1200px; height: 716px; overflow: hidden; }
  body { background: var(--page); position: relative; font-family: "Roboto", Arial, sans-serif; }

  .card {
    position: absolute;
    top: 198px;
    width: 520px;
    height: 320px;
    border-radius: 4px;
    overflow: hidden;
    box-shadow: 0 10px 24px rgba(0,0,0,.22);
  }

  /* Back */
  .card-back {
    left: 60px; background: var(--card-black);
    display: flex; flex-direction: column; align-items: center; justify-content: center; gap: 22px;
  }
  .back-mark {
    display: flex; align-items: center; gap: 16px;
    font-family: "Libre Baskerville", Georgia, serif;
    font-size: 36px; color: var(--gold); letter-spacing: 1px;
  }
  .back-mark .mark-dot { width: 44px; height: 44px; border-radius: 50%; background: var(--gold); flex: none; }
  .back-services {
    font-size: 14px; font-weight: 500; color: var(--gold); letter-spacing: 1px;
  }

  /* Front */
  .card-front { left: 620px; background: var(--card-charcoal); color: var(--text-light); }
  .front-bands { position: absolute; inset: 0; }

  .brand { position: absolute; top: 34px; left: 36px; display: flex; align-items: center; gap: 12px; }
  .brand .mark-dot { width: 30px; height: 30px; border-radius: 50%; background: var(--gold); flex: none; }
  .brand-name {
    font-family: "Libre Baskerville", Georgia, serif;
    color: var(--gold); font-weight: 400; line-height: 1.25;
    font-size: 24px;
  }
  .brand-name span { display: block; font-size: 12px; letter-spacing: 4px; text-transform: uppercase; }

  .rule { position: absolute; top: 128px; left: 36px; width: 320px; height: 1.5px; background: var(--gold-soft); }

  .contacts { position: absolute; top: 146px; left: 36px; list-style: none; font-size: 12.5px; }
  .contacts li { display: flex; align-items: center; gap: 9px; height: 21px; }
  .contacts svg { width: 13px; height: 13px; flex: none; }

  .person { position: absolute; top: 146px; right: 28px; text-align: right; }
  .person-name { font-family: "Libre Baskerville", Georgia, serif; color: var(--gold); font-size: 20px; }
  .person-title { font-size: 11px; color: var(--text-light); margin-top: 2px; }
  .address { margin-top: 12px; font-size: 12.5px; line-height: 1.5; }

  .services {
    position: absolute; right: 26px; bottom: 11px;
    font-size: 12.5px; font-weight: 500; color: var(--ink); letter-spacing: .3px;
  }
</style>
</head>
<body>

  <section class="card card-back" aria-label="Card back">
    <div class="back-mark"><span class="mark-dot"></span>Harborline Crest</div>
    <div class="back-services">Auto | Home | Business | Life</div>
  </section>

  <section class="card card-front" aria-label="Card front">
    <svg class="front-bands" viewBox="0 0 520 320" preserveAspectRatio="none" aria-hidden="true">
      <defs>
        <linearGradient id="silver" x1="0" y1="0" x2="1" y2="0">
          <stop offset="0" stop-color="#8c8c8c"/>
          <stop offset=".5" stop-color="#e9e9e9"/>
          <stop offset="1" stop-color="#8c8c8c"/>
        </linearGradient>
      </defs>
      <polygon points="0,266 240,266 226,282 0,282" fill="url(#silver)"/>
      <polygon points="240,280 520,280 520,320 206,320" fill="#f5c829"/>
    </svg>

    <div class="brand">
      <span class="mark-dot"></span>
      <div class="brand-name">Harborline Crest<span>Insurance Services</span></div>
    </div>

    <div class="rule"></div>

    <ul class="contacts">
      <li>
        <svg viewBox="0 0 14 14"><rect width="14" height="14" rx="2" fill="#e8b423"/><path d="M4 3.5h2l.7 2-1.2.8a5 5 0 0 0 2.2 2.2l.8-1.2 2 .7v2c0 .5-.4.8-.9.8A6.6 6.6 0 0 1 3.2 4.4c0-.5.3-.9.8-.9z" fill="#1a1a1a"/></svg>
        +1 310 555 0142
      </li>
      <li>
        <svg viewBox="0 0 14 14"><rect width="14" height="14" rx="2" fill="#e8b423"/><rect x="4.5" y="2.5" width="5" height="9" rx="1" fill="none" stroke="#1a1a1a" stroke-width="1.2"/><circle cx="7" cy="10" r=".6" fill="#1a1a1a"/></svg>
        +1 310 555 0187
      </li>
      <li>
        <svg viewBox="0 0 14 14"><rect width="14" height="14" rx="2" fill="#e8b423"/><rect x="2.5" y="4" width="9" height="6.5" fill="none" stroke="#1a1a1a" stroke-width="1.1"/><path d="M2.5 4l4.5 3.5L11.5 4" fill="none" stroke="#1a1a1a" stroke-width="1.1"/></svg>
        daniel@harborlinecrest.com
      </li>
    </ul>

    <div class="person">
      <div class="person-name">Daniel Reyes</div>
      <div class="person-title">Managing Director</div>
      <div class="address">4127 Linden Ave No.210<br>Glendale California 91203</div>
    </div>

    <div class="services">Auto | Home | Business | Life</div>
  </section>

</body>
</html>
```